Varnath Consulting Business card design.

See our website www.varnathconsulting-example.com which will give you a good idea of what we are about. The font is called 'Play'.

I'd like a standout business card in keeping with the themes and branding on the website

Target Market(s)

professionals. HR directors

Industry/Entity Type

Business

Contact Information for Business Card

Varnath Consulting PO Box 3917 Tindale Creek NSW 2840 1300 457 318 Gerald Ashbury Principal email: jobs@varnathconsulting-example.com ABN: 31792048663

Font styles to use
Other font styles liked:
• Play

Requirements
Must have
• Must have same design colours and branding as website.
• On back I'd prefer a list of the things we do which appears below the name at the header on the website

```html
<!DOCTYPE html>
<html lang="en">
<head>
<meta charset="utf-8">
<title>Varnath Consulting – Business Card</title>
<link rel="stylesheet" href="https://fonts.googleapis.com/css2?family=Play:wght@400;700&display=swap">
<style>
  :root {
    --navy-deep: #051430;
    --navy: #0a1f40;
    --photo-blue: #1d4b7c;
    --photo-light: #3f73a6;
    --accent: #3da5f4;
    --white: #ffffff;
  }
  * { margin: 0; padding: 0; box-sizing: border-box; }
  html, body {
    width: 1200px;
    height: 741px;
    overflow: hidden;
    background: var(--navy-deep);
  }
  .card {
    position: relative;
    width: 1200px;
    height: 741px;
    overflow: hidden;
    background: var(--navy-deep);
    font-family: 'Play', sans-serif;
    color: var(--white);
  }
  .card__photo {
    position: absolute;
    top: 0;
    right: 0;
    width: 720px;
    height: 741px;
    background:
      linear-gradient(90deg, var(--navy-deep) 0%, rgba(5,20,48,0.6) 22%, rgba(5,20,48,0) 50%),
      radial-gradient(ellipse at 70% 45%, var(--photo-light) 0%, var(--photo-blue) 45%, var(--navy) 100%);
  }
  .brand {
    position: absolute;
    left: 138px;
    top: 118px;
    font-size: 44px;
    font-weight: 400;
    letter-spacing: 1px;
    color: var(--white);
  }
  .person {
    position: absolute;
    left: 140px;
    top: 220px;
  }
  .person__name {
    font-size: 42px;
    line-height: 46px;
    font-weight: 400;
    letter-spacing: 0.5px;
  }
  .person__title {
    font-size: 26px;
    line-height: 26px;
  }
  .contact {
    position: absolute;
    left: 140px;
    font-size: 31px;
    line-height: 36px;
    letter-spacing: 0.5px;
  }
  .contact--phone { top: 320px; }
  .contact--address { top: 384px; }
  .contact--email { top: 482px; }
  .contact--abn { top: 545px; }
  .icon {
    position: absolute;
    left: 86px;
  }
  .icon--phone { top: 316px; }
  .icon--pin { top: 394px; }
  .icon--email { top: 478px; }
</style>
</head>
<body>
  <div class="card">
    <div class="card__photo" role="img" aria-label="Blue-toned photograph of sprinters' hands at the starting line"></div>

    <div class="brand">VARNATH CONSULTING</div>

    <div class="person">
      <div class="person__name">Gerald Ashbury</div>
      <div class="person__title">Principal</div>
    </div>

    <svg class="icon icon--phone" width="48" height="48" viewBox="0 0 24 24" aria-hidden="true">
      <path fill="#3da5f4" d="M6.6 10.8c1.4 2.8 3.8 5.1 6.6 6.6l2.2-2.2c.3-.3.7-.4 1-.2 1.1.4 2.3.6 3.6.6.6 0 1 .4 1 1V20c0 .6-.4 1-1 1C10.6 21 3 13.4 3 4c0-.6.4-1 1-1h3.5c.6 0 1 .4 1 1 0 1.3.2 2.5.6 3.6.1.3 0 .7-.2 1z"/>
    </svg>
    <div class="contact contact--phone">1300 457 318</div>

    <svg class="icon icon--pin" width="34" height="52" viewBox="0 0 24 36" aria-hidden="true">
      <path fill="#3da5f4" d="M12 0C5.4 0 0 5.4 0 12c0 9 12 24 12 24s12-15 12-24C24 5.4 18.6 0 12 0zm0 16.5a4.5 4.5 0 1 1 0-9 4.5 4.5 0 0 1 0 9z"/>
    </svg>
    <div class="contact contact--address">PO Box 3917<br>Tindale Creek NSW 2840</div>

    <svg class="icon icon--email" width="46" height="46" viewBox="0 0 46 46" aria-hidden="true">
      <circle cx="23" cy="23" r="23" fill="#3da5f4"/>
      <rect x="11" y="15" width="24" height="16" fill="none" stroke="#051430" stroke-width="2"/>
      <path d="M11 15l12 10 12-10M11 31l9-8M35 31l-9-8" fill="none" stroke="#051430" stroke-width="2"/>
    </svg>
    <div class="contact contact--email">jobs@varnathconsulting-example.com</div>

    <div class="contact contact--abn">ABN: 31792048663</div>
  </div>
</body>
</html>
```